Letterhead and Business Card for our company

We need a letterhead to our company with Business Cards.. This will be printed. The letter head is the official use for the company.

Note: Put in consideration that 2 languages will be used, you will design the English and we will add the Arabic.

Company name: Tidewell Partners
City: Jeddah
District: Alrehab
Center: Marlow Square
Country: Saudi Arabia
POBox: 7382 Jeddah 29813

Industry/Entity Type

Startup

Font styles to use
Sans Serif

Requirements
Must have
• Capital: 100,000
• CR: 5817209364

```html
<!DOCTYPE html>
<html lang="en">
<head>
<meta charset="utf-8">
<title>Tidewell Partners — Letterhead and Business Cards</title>
<link href="https://fonts.googleapis.com/css2?family=Open+Sans:wght@400;600&display=swap" rel="stylesheet">
<style>
  :root {
    --bg: #f1f1f1;
    --paper: #ffffff;
    --ink: #222222;
    --ink-soft: #555555;
    --rule: #d4d4d4;
    --night: #141414;
    --cyan: #2aa6d8;
    --green: #8cc63f;
    --magenta: #e0267f;
    --watermark: #ececec;
  }
  * { box-sizing: border-box; margin: 0; padding: 0; }
  html, body { width: 1200px; height: 798px; overflow: hidden; }
  body {
    background: var(--bg);
    font-family: "Open Sans", Arial, sans-serif;
    color: var(--ink);
    position: relative;
  }

  /* Brand lockup */
  .brand { display: flex; align-items: center; gap: 8px; }
  .brand-dot { width: 22px; height: 22px; border-radius: 50%; background: var(--cyan); flex: none; }
  .brand-name { font-weight: 600; font-size: 15px; letter-spacing: 0.04em; text-transform: uppercase; color: var(--ink); line-height: 1.1; }

  /* Accent strip */
  .accent-strip { display: flex; height: 5px; }
  .accent-strip .base { flex: 1; background: var(--night); }
  .accent-strip span:not(.base) { width: 34px; }
  .accent-strip .c { background: var(--cyan); }
  .accent-strip .g { background: var(--green); }
  .accent-strip .m { background: var(--magenta); }

  /* Letterhead */
  .letterhead {
    position: absolute; left: 60px; top: 28px;
    width: 524px; height: 742px;
    background: var(--paper);
    box-shadow: 0 1px 4px rgba(0,0,0,0.12);
    padding: 52px 52px 0;
    overflow: hidden;
  }
  .letterhead .brand { margin-bottom: 40px; }
  .watermark {
    position: absolute; right: 40px; top: 300px;
    width: 200px; height: 200px; border-radius: 50%;
    background: var(--watermark);
  }
  .letter { position: relative; font-size: 9.5px; line-height: 1.55; color: var(--ink-soft); }
  .letter p { margin-bottom: 13px; }
  .letter .address { margin-bottom: 16px; }
  .signature {
    width: 110px; height: 28px; margin: 10px 0 2px;
    background: linear-gradient(90deg, #cfcfcf, #e8e8e8);
    border-radius: 3px;
  }
  .letter .role { color: var(--ink); }
  .letter-footer {
    position: absolute; left: 0; right: 0; bottom: 0;
  }
  .letter-footer .details {
    padding: 0 52px 10px; font-size: 7.5px; color: var(--ink-soft);
    text-align: right; line-height: 1.6;
  }

  /* Business cards */
  .card {
    position: absolute; width: 350px; height: 200px;
    box-shadow: 0 1px 4px rgba(0,0,0,0.15);
    overflow: hidden;
  }
  .card-front {
    left: 700px; top: 110px;
    background: var(--night);
    display: flex; align-items: center; justify-content: center;
  }
  .card-front .brand-dot { width: 40px; height: 40px; }
  .card-front .brand-name { color: #ffffff; font-size: 24px; }
  .card-front .brand { gap: 14px; }

  .card-back {
    left: 700px; top: 440px;
    background: var(--paper);
    padding: 24px 28px 0;
  }
  .card-back .brand { justify-content: flex-end; margin-bottom: 24px; }
  .card-back .brand-name { font-size: 12px; }
  .card-back .brand-dot { width: 16px; height: 16px; }
  .person { font-size: 11px; font-weight: 600; text-transform: uppercase; letter-spacing: 0.06em; }
  .person-role { font-size: 8px; color: var(--ink-soft); margin-bottom: 10px; }
  .contact { list-style: none; font-size: 8px; color: var(--ink-soft); line-height: 1.9; }
  .contact li { display: flex; align-items: center; gap: 6px; }
  .contact svg { width: 9px; height: 9px; fill: var(--cyan); flex: none; }
  .card-back .accent-strip { position: absolute; left: 0; right: 0; bottom: 0; }
</style>
</head>
<body>

<article class="letterhead">
  <div class="watermark" aria-hidden="true"></div>
  <header class="brand">
    <span class="brand-dot"></span>
    <span class="brand-name">Tidewell Partners</span>
  </header>

  <section class="letter">
    <p class="address">November 1, 2015<br>Mr. Dalton Reyes<br>88 Harbour Row<br>Norwich, U.K. 40921</p>
    <p>Dear Mr. Reyes</p>
    <p>The first paragraph of a typical business letter is used to state the main point of the letter. Begin with a friendly opening, then quickly transition into the purpose of your letter. Use a couple of sentences to explain the purpose, but do not go in to detail until the next paragraph.</p>
    <p>Beginning with the second paragraph, state the supporting details to justify your purpose. These may take the form of background information, statistics or first-hand accounts. A few short paragraphs within the body of the letter should be enough to support your reasoning. Finally, in the closing paragraph, briefly restate your purpose and why it is important.</p>
    <p>Finally, in the closing paragraph, briefly restate your purpose and why it is important. If the purpose of your letter is related to your employment, consider ending your letter with your contact information and title. However, if the purpose is informational, think about closing with gratitude for the reader's time.</p>
    <p>Sincerely,</p>
    <div class="signature" role="img" aria-label="Handwritten signature of the company president"></div>
    <p class="role">President</p>
  </section>

  <footer class="letter-footer">
    <p class="details">POBox: 7382 Jeddah 29813 - Marlow Square, Alrehab - Saudi Arabia | info@tidewellpartners.sa | www.tidewellpartners.sa<br>Capital: 100,000 | CR: 5817209364</p>
    <div class="accent-strip"><span class="base"></span><span class="c"></span><span class="g"></span><span class="m"></span></div>
  </footer>
</article>

<section class="card card-front">
  <div class="brand">
    <span class="brand-dot"></span>
    <span class="brand-name">Tidewell Partners</span>
  </div>
</section>

<section class="card card-back">
  <div class="brand">
    <span class="brand-dot"></span>
    <span class="brand-name">Tidewell Partners</span>
  </div>
  <p class="person">Karim Nasser</p>
  <p class="person-role">Managing Director</p>
  <ul class="contact">
    <li><svg viewBox="0 0 10 10"><path d="M2 0h2l1 3-1.5 1a6 6 0 0 0 2.5 2.5L7 5l3 1v2l-1 2C4 10 0 6 0 1z"/></svg>+966 12 581 7209</li>
    <li><svg viewBox="0 0 10 10"><path d="M0 2h10v6H0zM0 2l5 3.5L10 2"/></svg>info@tidewellpartners.sa</li>
    <li><svg viewBox="0 0 10 10"><circle cx="5" cy="5" r="4.5"/></svg>www.tidewellpartners.sa</li>
    <li><svg viewBox="0 0 10 10"><path d="M5 0a3.5 3.5 0 0 1 3.5 3.5C8.5 6 5 10 5 10S1.5 6 1.5 3.5A3.5 3.5 0 0 1 5 0z"/></svg>POBox: 7382 Jeddah 29813 - Saudi Arabia</li>
  </ul>
  <div class="accent-strip"><span class="base"></span><span class="c"></span><span class="g"></span><span class="m"></span></div>
</section>

</body>
</html>
```